Bows Catalog Cover

Cover Page for a catalog for bows. Same logo MOR Morvane Alpina Cordaria.
Catalog overview: https://www.folioworks-demo.net/MOR-Morvane-Alpina-Cordaria/catalogs/MOR-catalog.html
No instruments, no scores, Only bows or bow parts (head, frog ...). Drawings or pictures.

Target Market(s)

Violin makers and reseller

Requirements
Must have
• bows or bow parts
Nice to have
• Drawings and or pictures
Should not have
• full Instruments or scores

```html
<!DOCTYPE html>
<html lang="fr">
<head>
<meta charset="utf-8">
<title>MOR Morvane Alpina Cordaria – Archets Catalogue 2021</title>
<link rel="stylesheet" href="https://fonts.googleapis.com/css2?family=Oswald:wght@600&family=Raleway:wght@300;400;700&display=swap">
<style>
  :root {
    --backdrop: #e3e3e5;
    --paper: #f3f3f4;
    --navy: #1f1c7c;
    --violet: #b463c2;
    --ink: #3a3a4a;
    --wood-soft: #e6d8d4;
    --wood-mid: #d9c2bb;
  }
  * { margin: 0; padding: 0; box-sizing: border-box; }
  html, body { width: 1200px; height: 1000px; overflow: hidden; }
  body {
    background: var(--backdrop);
    font-family: "Raleway", sans-serif;
    color: var(--ink);
  }
  .spread {
    position: absolute;
    left: 60px; top: 118px;
    width: 1080px; height: 764px;
    display: flex;
    box-shadow: 0 18px 40px rgba(0,0,0,0.18);
  }
  .page {
    position: relative;
    width: 540px; height: 764px;
    background: var(--paper);
    overflow: hidden;
  }
  .page--back { border-right: 1px solid #dcdcde; }

  /* Back cover */
  .back-mark {
    position: absolute;
    left: 0; right: 0; top: 170px;
    display: flex; align-items: center; justify-content: center; gap: 22px;
  }
  .back-mark__dot {
    width: 96px; height: 96px; border-radius: 50%;
    background: var(--navy);
  }
  .back-mark__name {
    font-weight: 700; font-size: 92px; letter-spacing: 4px;
    color: var(--navy);
  }
  .back-contact {
    position: absolute;
    left: 0; right: 0; top: 468px;
    text-align: center;
    font-style: normal;
    font-size: 10px; line-height: 1.45;
    color: var(--ink);
  }
  .back-contact__brand {
    display: inline-flex; align-items: center; gap: 6px;
    font-weight: 700; font-size: 24px; letter-spacing: 1px;
    color: var(--navy); margin-bottom: 6px;
  }
  .back-contact__brand::before {
    content: ""; width: 20px; height: 20px; border-radius: 50%;
    background: var(--navy);
  }
  .back-contact__company { letter-spacing: 1px; }
  .back-contact__gap { margin-top: 8px; }

  /* Front cover */
  .spine-rule {
    position: absolute;
    left: 48px; top: 0; bottom: 0;
    width: 6px; background: var(--navy);
  }
  .cover-title {
    position: absolute;
    left: 60px; bottom: 40px;
    transform-origin: left bottom;
    transform: rotate(-90deg) translateY(100%);
    font-family: "Oswald", sans-serif;
    font-weight: 600; font-size: 92px; line-height: 1;
    letter-spacing: 6px;
    color: var(--navy);
  }
  .cover-brand {
    position: absolute;
    left: 66px; top: 28px;
    transform-origin: left top;
    transform: rotate(90deg) translateY(-100%);
    display: flex; align-items: center; gap: 10px;
    font-weight: 700; font-size: 44px; letter-spacing: 3px;
    color: var(--navy);
    white-space: nowrap;
  }
  .cover-brand::before {
    content: ""; width: 34px; height: 34px; border-radius: 50%;
    background: var(--navy);
  }
  .bow-visual {
    position: absolute;
    left: 220px; top: 110px;
    width: 270px; height: 440px;
    background: linear-gradient(160deg, var(--wood-soft) 0%, var(--wood-mid) 100%);
  }
  .cover-catalogue {
    position: absolute;
    right: 34px; bottom: 98px;
    text-align: right;
  }
  .cover-catalogue__label {
    font-weight: 400; font-size: 30px; letter-spacing: 1px;
    color: var(--navy);
  }
  .cover-catalogue__year {
    font-weight: 300; font-size: 46px; letter-spacing: 2px;
    color: var(--violet); line-height: 1.15;
  }
  .cover-web {
    position: absolute;
    right: 34px; bottom: 36px;
    font-weight: 400; font-size: 15px; letter-spacing: 1px;
    color: #555;
  }
</style>
</head>
<body>
  <div class="spread">
    <section class="page page--back">
      <div class="back-mark">
        <span class="back-mark__dot"></span>
        <span class="back-mark__name">MOR</span>
      </div>
      <address class="back-contact">
        <div class="back-contact__brand">MOR</div>
        <div class="back-contact__company">MORVANE ALPINA CORDARIA</div>
        <div>7, chemin des Aulnes - 38950 Valbrune sur Isère</div>
        <div>FRANCE</div>
        <div class="back-contact__gap">Tél : +33 (0)4.00.12.34.56</div>
        <div>contact@morvane-cordaria.example</div>
        <div>atelier.morvane@postmail.example</div>
      </address>
    </section>

    <section class="page page--front">
      <div class="spine-rule"></div>
      <div class="cover-brand">MOR</div>
      <h1 class="cover-title">ARCHETS</h1>
      <div class="bow-visual" role="img" aria-label="Photograph of a pernambuco violin bow laid diagonally, head at top, frog at bottom"></div>
      <div class="cover-catalogue">
        <div class="cover-catalogue__label">CATALOGUE</div>
        <div class="cover-catalogue__year">2021</div>
      </div>
      <div class="cover-web">morvane-alpina-cordaria.example</div>
    </section>
  </div>
</body>
</html>
```